Banner for homepage

It is a new banner for the homepage, temporary site address is 203.0.113.57 ( is the biggest banner only ) . Would be 5 variations for image content as below (in Portuguese ) :

Image 1:
Leitor de codigo de barras
Todos os tipos de leitores de código de barras para as mais diversas aplicações.
( example of product images in : http://www.quorvelidx.com/en-US/Pages/Category.aspx?category=barcode-scanners&cat=QMT)

Image 2:
Impressora de etiquetas
Identifique o que for nessário com o melhor custo/beneficio e flexibilidade de materiais de impressão.
( example of product images in : tarnix.com in label printers desktop and industrial)

Image 3:
Impressora de cupom
Imprima recibos e cupons fiscais com agilidade e qualidade, temos a impressora certa para o seu PDV.
( example of product images in : http://www.plivorato.com.br/equipamento-categoria-impressoras+fiscais.html)

Image 4:
Coletor de dados
Computadores móveis com leitor de código de barras, que levam a automação para frente de trabalho.
( example of product images in : http://www.quorvelidx.com/en-US/Pages/Category.aspx?cat=QMT&category=hand-held-mobile-computer)

Image 5:
Etiquetas e Ribbons:
Etiquetas adesivas e não adesivas em vários de tipos de materiais, papéis e plásticos. O ribbon certo para impressão perfeita em cada material.
( example of product images in : http://www.lumetrask.com/cats/supplies/barcode-printer.htm?nav=hdr)

```html
<!DOCTYPE html>
<html lang="pt-BR">
<head>
<meta charset="utf-8">
<title>Leitor de Código de Barras</title>
<link rel="stylesheet" href="https://fonts.googleapis.com/css2?family=Arimo:wght@400;700&display=swap">
<style>
  :root {
    --page-bg: #ffffff;
    --panel-light: #f4f4f4;
    --panel-mid: #dcdcdc;
    --panel-dark: #c4c4c4;
    --panel-border: #b9b9b9;
    --stripe: rgba(255,255,255,0.35);
    --title-white: #ffffff;
    --title-red: #c4161c;
    --body-text: #3a3a3a;
    --button-top: #e23a3a;
    --button-bottom: #a80f14;
    --button-border: #8a0a0e;
    --person-tone-a: #9aa0a8;
    --person-tone-b: #4c5058;
    --device-tone-a: #f2f2f2;
    --device-tone-b: #8c8c8c;
  }
  * { margin: 0; padding: 0; box-sizing: border-box; }
  html, body {
    width: 1200px; height: 548px; overflow: hidden;
    background: var(--page-bg);
    font-family: "Arimo", Arial, sans-serif;
  }
  .banner {
    position: relative;
    width: 1200px; height: 548px;
    border: 3px solid var(--panel-border);
    border-radius: 22px;
    overflow: hidden;
    background:
      repeating-linear-gradient(135deg, var(--stripe) 0 2px, transparent 2px 7px),
      linear-gradient(160deg, var(--panel-light) 0%, var(--panel-mid) 55%, var(--panel-dark) 100%);
  }
  .person-photo {
    position: absolute; left: 34px; top: 9px;
    width: 334px; height: 539px;
    border-radius: 40% 40% 0 0 / 18% 18% 0 0;
    background: linear-gradient(180deg, var(--person-tone-a) 0%, var(--person-tone-b) 100%);
  }
  .scanner-photo {
    position: absolute; left: 813px; top: 43px;
    width: 368px; height: 445px;
    border-radius: 30% 20% 40% 40%;
    background: radial-gradient(ellipse at 40% 35%, var(--device-tone-a) 0%, var(--device-tone-b) 100%);
  }
  .headline {
    position: absolute; left: 298px; top: 96px;
    font-weight: 700; line-height: 1;
  }
  .headline-top {
    display: block; font-size: 54px; color: var(--title-white);
    text-shadow: 0 2px 3px rgba(0,0,0,0.45);
  }
  .headline-main {
    display: block; font-size: 62px; color: var(--title-red);
    margin-top: 6px;
    text-shadow: 0 1px 1px rgba(255,255,255,0.6);
  }
  .tagline {
    position: absolute; left: 428px; top: 252px;
    font-size: 33px; line-height: 39px; color: var(--body-text);
  }
  .cta {
    position: absolute; left: 479px; top: 442px;
    width: 245px; height: 75px;
    display: flex; align-items: center; justify-content: center;
    border: 2px solid var(--button-border);
    border-radius: 9px;
    background: linear-gradient(180deg, var(--button-top) 0%, var(--button-bottom) 100%);
    box-shadow: 0 3px 6px rgba(0,0,0,0.35);
    color: #fff; font-weight: 700; font-size: 29px;
    text-decoration: none;
    text-shadow: 0 1px 2px rgba(0,0,0,0.4);
  }
</style>
</head>
<body>
  <section class="banner">
    <div class="person-photo" role="img" aria-label="Mulher de terno cinza segurando um leitor de código de barras"></div>
    <div class="scanner-photo" role="img" aria-label="Leitor de código de barras de mão, branco e cinza"></div>
    <h1 class="headline">
      <span class="headline-top">Leitor De</span>
      <span class="headline-main">Codigo de Barras</span>
    </h1>
    <p class="tagline">Todos os tipos de leitores<br>de codigo de barras para as<br>maias diversas aplicacoes</p>
    <a class="cta" href="#">Veja Mais</a>
  </section>
</body>
</html>
```